Veltrionix Knowledge Enhancement Company Website

Veltrionix is knowledge enhancement Highend and Deep Technology Company who has training programs in Applied Quantum, Applied Artificial Intelligence and Data Science. All the technologies are very advanced and future technologies and the website should reflect the technology advancement. Looking for a sophisticated web design which will reflect our focus on deep and future technologies. Logo file is uploaded

Target Market(s)

Big Corporates and Premium Colleges

Industry/Entity Type

Technology, Deep Technology, Future Technology

Coding

Coded - Design and coding required

Number of Pages Required

5+ page

Requirements
Must have
• A Very Contemporary clean look and should reflect Future Technologies
Nice to have
• Should be very Classy
Should not have
• Traditional Fonts and Colors

```html
<!DOCTYPE html>
<html lang="en">
<head>
<meta charset="utf-8">
<title>Veltrionix – Training Calendar</title>
<link href="https://fonts.googleapis.com/css2?family=Poppins:wght@400;500;600&family=Oswald:wght@500&family=EB+Garamond:wght@600;700&display=swap" rel="stylesheet">
<style>
:root{
  --navy:#0a2340;
  --navy-deep:#061a30;
  --blue:#29a9e1;
  --orange:#fb9a0e;
  --ink:#1c1c1c;
  --footer-bg:#e1f2fa;
  --white:#ffffff;
}
*{margin:0;padding:0;box-sizing:border-box}
html,body{width:907px;height:1200px;overflow:hidden;background:var(--white)}
body{position:relative;font-family:'Poppins',sans-serif;color:var(--ink)}
.hero{position:absolute;left:0;top:0;width:907px;height:320px;overflow:hidden}
.hero-art{position:absolute;inset:0;background:
  radial-gradient(circle at 443px 205px,#ffb36b 0,#e06b2a 18px,rgba(80,90,140,.6) 60px,rgba(20,60,110,0) 140px),
  radial-gradient(ellipse at 540px 250px,rgba(190,120,90,.55) 0,rgba(10,35,64,0) 200px),
  radial-gradient(ellipse at 330px 250px,rgba(120,170,210,.45) 0,rgba(10,35,64,0) 180px),
  linear-gradient(180deg,var(--navy-deep),var(--navy) 60%,#163a5e)}
.wave{position:absolute;left:0;bottom:0;width:907px;height:30px}
.brand{position:absolute;left:107px;top:30px;display:flex;align-items:center;gap:6px;color:var(--blue);font-weight:600;font-size:19px}
.brand-mark{width:14px;height:14px;background:var(--blue)}
.nav{position:absolute;top:28px;left:283px;display:flex;gap:0;font-size:9.3px;color:var(--white)}
.nav a{color:inherit;text-decoration:none;margin-right:15px;line-height:14px}
.nav a.active{color:var(--orange);font-weight:500}
.btn-contact{position:absolute;left:731px;top:21px;width:69px;height:27px;background:var(--orange);color:var(--white);font-size:9.3px;display:flex;align-items:center;justify-content:center;border-radius:2px}
.hero-title{position:absolute;top:103px;width:907px;text-align:center;font-family:'Oswald',sans-serif;font-size:25px;color:var(--white);letter-spacing:.3px}
.crumb{position:absolute;top:138px;width:907px;text-align:center;font-size:12px;color:var(--white)}
.section-mark{position:absolute;left:443px;top:388px;width:20px;height:20px;background:var(--blue)}
.eyebrow{position:absolute;top:419px;width:907px;text-align:center;font-size:13.5px}
.section-title{position:absolute;top:442px;width:907px;text-align:center;font-family:'EB Garamond',serif;font-weight:700;font-size:30px;color:var(--blue);letter-spacing:.2px}
.event{position:absolute;display:flex;align-items:center}
.date{width:80px;height:80px;background:var(--blue);color:var(--white);text-align:center;padding-top:12px}
.date .day{font-size:29px;font-weight:500;line-height:32px}
.date .mon{font-size:12.5px;font-weight:500;margin-top:5px}
.courses{list-style:none;margin-left:16px;font-size:10.3px}
.courses li{display:flex;align-items:center;height:22px}
.courses li::before{content:"";width:5px;height:5px;border-radius:50%;background:var(--orange);margin-right:7px}
.footer{position:absolute;left:0;top:890px;width:907px;height:277px;background:var(--footer-bg)}
.foot-head{position:absolute;top:66px;font-family:'EB Garamond',serif;font-weight:600;font-size:13px;letter-spacing:.2px}
.links{position:absolute;left:107px;top:98px;list-style:none;font-size:9.3px}
.links li{height:20.2px;display:flex;align-items:center}
.links li::before{content:"›";margin-right:6px;font-size:10px}
.links li.active{color:var(--orange);font-weight:500}
.contact{position:absolute;left:250px;top:98px;font-size:10px}
.contact-item{display:flex;gap:9px;margin-bottom:10px}
.contact-icon{width:22px;height:22px;border-radius:50%;background:var(--blue);flex:none;display:flex;align-items:center;justify-content:center}
.contact-item b{display:block;font-size:11px;font-weight:600}
.contact-item p{line-height:15.5px}
.social{position:absolute;left:470px;top:98px;list-style:none;font-size:10px}
.social li{display:flex;align-items:center;height:36.5px}
.social li::before{content:"";width:21px;height:21px;border:1px solid #333;border-radius:50%;margin-right:10px}
.foot-brand{position:absolute;left:612px;top:120px;display:flex;align-items:center;gap:10px;color:var(--blue);font-weight:600;font-size:32px}
.foot-brand span.sq{width:30px;height:30px;background:var(--blue)}
.copyright{position:absolute;left:0;top:1167px;width:907px;height:33px;background:var(--blue);color:var(--white);font-size:10px;display:flex;align-items:center;justify-content:center}
</style>
</head>
<body>
<header class="hero">
  <div class="hero-art" role="img" aria-label="Robotic hand and human finger touching amid glowing circuit lines and binary code"></div>
  <svg class="wave" viewBox="0 0 907 30" preserveAspectRatio="none"><path d="M0 8 C60 -2 90 20 200 12 C320 4 420 30 480 18 C560 2 640 26 760 18 C830 14 880 8 907 0 L907 30 L0 30 Z" fill="#fff"/></svg>
  <div class="brand"><span class="brand-mark"></span>Veltrionix</div>
  <nav class="nav">
    <a>About Us</a><a>Courses We Offer</a><a class="active">Training Calendar</a><a>Trainee Enrollment</a><a>Become Our Trainer</a>
  </nav>
  <div class="btn-contact">Contact Us</div>
  <h1 class="hero-title">Training Calendar</h1>
  <div class="crumb">Home &nbsp;»&nbsp; Training Calendar</div>
</header>

<main>
  <div class="section-mark"></div>
  <p class="eyebrow">Our Schedule</p>
  <h2 class="section-title">TRAINING CALENDAR 2023-24</h2>

  <div class="event" style="left:107px;top:510px"><div class="date"><div class="day">21</div><div class="mon">Jan</div></div>
    <ul class="courses"><li>Data Science</li><li>Applied Artificial Intelligence</li></ul></div>
  <div class="event" style="left:453px;top:509px"><div class="date"><div class="day">22</div><div class="mon">Jan</div></div>
    <ul class="courses"><li>Applied Quantum</li></ul></div>
  <div class="event" style="left:107px;top:629px"><div class="date"><div class="day">11</div><div class="mon">Feb</div></div>
    <ul class="courses"><li>Data Science</li><li>Applied Artificial Intelligence</li><li>Applied Quantum</li></ul></div>
  <div class="event" style="left:453px;top:629px"><div class="date"><div class="day">18</div><div class="mon">Feb</div></div>
    <ul class="courses"><li>Applied Artificial Intelligence</li></ul></div>
  <div class="event" style="left:107px;top:749px"><div class="date"><div class="day">19</div><div class="mon">Feb</div></div>
    <ul class="courses"><li>Applied Artificial Intelligence</li><li>Applied Quantum</li></ul></div>
  <div class="event" style="left:453px;top:749px"><div class="date"><div class="day">01</div><div class="mon">Mar</div></div>
    <ul class="courses"><li>Data Science</li><li>Applied Artificial Intelligence</li><li>Applied Quantum</li></ul></div>
</main>

<footer class="footer">
  <h3 class="foot-head" style="left:107px">QUICK LINKS</h3>
  <ul class="links">
    <li>Home</li><li>About Us</li><li>Courses We Offer</li><li class="active">Training Calendar</li><li>Trainee Enrollment</li><li>Become Our Trainer</li><li>Contact Us</li>
  </ul>
  <h3 class="foot-head" style="left:250px">CONTACT DETAILS</h3>
  <div class="contact">
    <div class="contact-item"><span class="contact-icon"><svg width="10" height="12" viewBox="0 0 10 12"><path d="M5 0a4 4 0 0 0-4 4c0 3 4 8 4 8s4-5 4-8a4 4 0 0 0-4-4z" fill="#fff"/><circle cx="5" cy="4" r="1.5" fill="#29a9e1"/></svg></span>
      <div><b>Address</b><p>12 Lorem Imsum, Street Name,<br>City Name, Country - 12345</p></div></div>
    <div class="contact-item"><span class="contact-icon"><svg width="11" height="11" viewBox="0 0 24 24"><path d="M6.6 10.8a15 15 0 0 0 6.6 6.6l2.2-2.2a1 1 0 0 1 1-.25 11.4 11.4 0 0 0 3.6.57 1 1 0 0 1 1 1V20a1 1 0 0 1-1 1A17 17 0 0 1 3 4a1 1 0 0 1 1-1h3.5a1 1 0 0 1 1 1c0 1.25.2 2.45.57 3.57a1 1 0 0 1-.25 1z" fill="#fff"/></svg></span>
      <div><b>Phone</b><p>123.456.7890</p></div></div>
    <div class="contact-item"><span class="contact-icon"><svg width="11" height="9" viewBox="0 0 11 9"><rect width="11" height="9" rx="1" fill="#fff"/><path d="M0.5 1 L5.5 5 L10.5 1" stroke="#29a9e1" fill="none"/></svg></span>
      <div><b>Email</b><p>info@veltrionix.com</p></div></div>
  </div>
  <h3 class="foot-head" style="left:470px">FOLLOW US ON</h3>
  <ul class="social"><li>Friendly</li><li>Chirper</li><li>Linkwork</li><li>Viewtube</li></ul>
  <div class="foot-brand"><span class="sq"></span>Veltrionix</div>
</footer>
<div class="copyright">© 2023 Veltrionix. All Rights Reserved.</div>
</body>
</html>
```